Business Card Design Project

Recently had a new logo made up for my company and new business cards done as well. I have attached the logos for your viewing. Additional projects may be needed. Good luck!

Industry/Entity Type

Business

```html
<!DOCTYPE html>
<html lang="en">
<head>
<meta charset="utf-8">
<title>Whitmore Financial Group – Business Card</title>
<link rel="stylesheet" href="https://fonts.googleapis.com/css2?family=Roboto+Condensed:wght@400;500&display=swap">
<style>
  :root {
    --backdrop: #2e2e31;
    --card-navy: #24253a;
    --card-navy-light: #33354d;
    --gold: #cfb97c;
    --ink-light: #ecebf0;
    --rule: #a08d5a;
  }
  * { margin: 0; padding: 0; box-sizing: border-box; }
  html, body {
    width: 1200px; height: 900px; overflow: hidden;
    background: var(--backdrop);
    font-family: "Roboto Condensed", "Arial Narrow", sans-serif;
  }
  .stage {
    position: relative; width: 1200px; height: 900px;
    display: flex; justify-content: center; align-items: center; gap: 110px;
  }
  .card {
    position: relative; width: 360px; height: 630px;
    background: radial-gradient(ellipse at 50% 40%, var(--card-navy-light), var(--card-navy) 75%);
    box-shadow: 0 14px 34px rgba(0,0,0,.45);
    overflow: hidden;
  }
  .card__band {
    position: absolute; left: 0; right: 0; bottom: 0; height: 12px;
    background: var(--gold);
  }

  /* front */
  .card--front { padding: 48px 34px 0 34px; }
  .brand { display: flex; align-items: center; gap: 14px; }
  .brand__square {
    width: 62px; height: 62px; flex: none;
    border: 4px solid var(--gold);
  }
  .brand__name {
    color: var(--gold); font-weight: 500; font-size: 19px;
    letter-spacing: 2px; line-height: 1.2; text-transform: uppercase;
  }
  .person { margin-top: 120px; }
  .person__name {
    color: var(--ink-light); font-weight: 500; font-size: 24px;
    letter-spacing: 3px; text-transform: uppercase;
  }
  .person__title {
    color: var(--ink-light); font-size: 15px; letter-spacing: 1px; margin-top: 6px;
  }
  .rule { height: 1px; background: var(--rule); margin: 20px 0; }
  .contact { display: grid; grid-template-columns: 64px 1fr; row-gap: 6px; font-size: 15px; letter-spacing: .8px; }
  .contact__label { color: var(--gold); }
  .contact__value { color: var(--ink-light); }
  .address { color: var(--ink-light); font-size: 15px; letter-spacing: 1px; line-height: 1.55; }
  .website { color: var(--gold); font-size: 15px; letter-spacing: 1px; margin-top: 14px; }

  /* back */
  .card--back { display: flex; flex-direction: column; align-items: center; justify-content: center; gap: 26px; padding-bottom: 12px; }
  .card--back .brand__square { width: 130px; height: 130px; border-width: 6px; }
  .card--back .brand__name { font-size: 20px; letter-spacing: 3px; text-align: center; }
</style>
</head>
<body>
<main class="stage">
  <section class="card card--front" aria-label="Business card front">
    <div class="brand">
      <div class="brand__square"></div>
      <div class="brand__name">Whitmore<br>Financial Group</div>
    </div>
    <div class="person">
      <h1 class="person__name">Daniel R. Whitmore</h1>
      <p class="person__title">Estate Planning and Insurance Specialist</p>
    </div>
    <div class="rule"></div>
    <div class="contact">
      <span class="contact__label">tel</span><span class="contact__value">555-210-4837</span>
      <span class="contact__label">fax</span><span class="contact__value">555-210-4902</span>
      <span class="contact__label">email</span><span class="contact__value">dwhitmore@whitmorefinancial.com</span>
    </div>
    <div class="rule"></div>
    <p class="address">4100 Harbor View Road, Suite 310E<br>Millbrook, New York 10577</p>
    <p class="website">www.whitmorefinancial.com</p>
    <div class="card__band"></div>
  </section>

  <section class="card card--back" aria-label="Business card back">
    <div class="brand__square"></div>
    <div class="brand__name">Whitmore<br>Financial Group</div>
    <div class="card__band"></div>
  </section>
</main>
</body>
</html>
```